Event for Hair Salon Wigs

We are introducing a new division of our hair salon selling hair wigs. We are introducing our clients to our wig line, which are beautiful well crafted wig. These wigs are not like granny's wigs, but wigs for women who want style and are willing to pay extra for beautiful believeable wigs. The event is casual were clients and there friends will be flowing in and out during a sunday afternoon.
The postcard should reflect a nice sunny spring day, but classy not extremely colorful. If you think a photo would add to a better look to the card....let me know and I will upload some.
Thank you

I have images that was uploaded, but have not been posted to this project. I'm not sure what's going on, but please look out for them. I have been trying to communicate with customer service, but no  response thus far. The cards I have received this far I think have to much of a colored pattern, I would love it if the logo "M Lovely Wigs" took center stage, rather than the word open house. Open House is important, but I don't won't it to be bolder than "wigs." Please leave room for address labels, and if possible, the description of the event should be in little bigger text. Oh, I am open to an abstract lady rather than the images that are uploaded, but if images are used, you don't have to use them all. Believe it or not...I do like simplicity:)

```html
<!DOCTYPE html>
<html lang="en">
<head>
<meta charset="utf-8">
<title>M Lovely Wigs – Event Postcard</title>
<link href="https://fonts.googleapis.com/css2?family=EB+Garamond:ital,wght@0,400;1,400&display=swap" rel="stylesheet">
<style>
  :root {
    --paper: #ffffff;
    --ink: #2a2a2a;
    --brand-red: #d8262e;
    --rule: #9a9a9a;
    --hair-dark: #5a3a24;
    --hair-light: #a8784e;
  }
  html, body {
    margin: 0;
    padding: 0;
    width: 1200px;
    height: 929px;
    overflow: hidden;
    background: var(--paper);
  }
  .postcard {
    position: relative;
    width: 1200px;
    height: 929px;
    background: var(--paper);
    font-family: "EB Garamond", Georgia, serif;
    font-style: italic;
    color: var(--ink);
  }
  .portrait {
    position: absolute;
    left: 54px;
    top: 42px;
    width: 136px;
    height: 192px;
    background: radial-gradient(ellipse at 50% 40%, var(--hair-light) 0%, var(--hair-dark) 65%, #ffffff 100%);
  }
  .salon-info {
    position: absolute;
    left: 230px;
    top: 46px;
    font-size: 22px;
    line-height: 26px;
  }
  .salon-info .salon-name { font-size: 27px; line-height: 32px; }
  .salon-info .web { margin-top: 22px; font-size: 18px; line-height: 24px; }
  .salon-info .phone { font-size: 18px; line-height: 24px; }
  .brand-mark {
    position: absolute;
    left: 622px;
    top: 44px;
    color: var(--brand-red);
    font-size: 50px;
    line-height: 1;
  }
  .message {
    position: absolute;
    left: 54px;
    top: 312px;
    width: 530px;
    font-size: 17.5px;
    line-height: 25px;
  }
  .message p { margin: 0 0 25px 0; }
  .message p.tight { margin: 0; }
  .address-area {
    position: absolute;
    left: 630px;
    top: 458px;
    width: 474px;
  }
  .address-area .to {
    position: absolute;
    left: 0;
    top: 0;
    font-size: 17px;
  }
  .address-area .line {
    position: absolute;
    left: 54px;
    width: 420px;
    border-top: 1px solid var(--rule);
  }
</style>
</head>
<body>
  <div class="postcard">
    <div class="portrait" role="img" aria-label="Photo of a woman wearing a short brown bob wig"></div>

    <div class="salon-info">
      <div class="salon-name">Salon M</div>
      <div>4810 Harbor View Dr, Ste. B</div>
      <div>Brookfield, CA 90000</div>
      <div class="web">www.mlovelywigs.com</div>
      <div class="phone">555 014-2287</div>
    </div>

    <div class="brand-mark">M Lovely Wigs</div>

    <div class="message">
      <p>Hello,</p>
      <p class="tight">I would like to cordially invite you to Salon M to introduce you to M Lovely Wigs. A showroom of some of the finest human and synthetic hair wigs available. Come look, feel and try-on these beautiful wigs. M Lovely Wigs can be purchased and ordered the day of the event for an introductory offer of 10% off of the total sales.</p>
      <p>If you bring a friend or donate a gently worn wig for charity, you will receive 15% off of the total purchase. Additionally, bring a friend and a gently worn wig and receive 20% off of the total purchase. Come join us... you might find a fabulous new look for spring!</p>
      <p>Hope to see you,</p>
      <p>Helen Marsh</p>
    </div>

    <div class="address-area">
      <span class="to">To:</span>
      <div class="line" style="top: 20px;"></div>
      <div class="line" style="top: 68px;"></div>
      <div class="line" style="top: 116px;"></div>
      <div class="line" style="top: 164px;"></div>
    </div>
  </div>
</body>
</html>
```